Advertising poster for a small Antenna business A3 in size

G,day my name is marcel .. im 30 years of age and i have only had my business for 5 months , the business is clean neat and professional and prides its self on results and quality customer service .
the business will be targeting ages of 20-80 years of age in a country town that is rapidly expanding .
I need a poster that speaks to the customer showing what I do and a friendly customer service .. preferably some sort of antenna installation on a roof and myself helping a customer in a family room environment to give that friendly vibe , need clean sleek photos eg plasma tv hung on a wall of a new contemporary home , well dressed customers and a professional looking installer and what ever else your creative mind imagination can come up with .

business name is " Marcels Antenna Service "
Phone number is 0491 32 60 47
services we provide
.new home antenna installations
.repair your dodgy reception
.wall mount your big screen TV's
.add extra outlets
.supply and install low cost security camera setups
.TELVIQ satellite installations
.anything tv related ,call marcel , he can do it !

please add the above text to the poster so that the customer knows what we do

The business's catchy phrase is "call marcel , he can do it "
provided will be just a photo of the van I drive .. I don't mind if the van is not in the poster .. but at least you will get an idea of whats going on, colors ect ect
I want to draw the customer in with the poster so they can look and read what we do and what we're all about .

```html
<!DOCTYPE html>
<html lang="en">
<head>
<meta charset="utf-8">
<title>Marcels Antenna Service – Poster</title>
<link rel="stylesheet" href="https://fonts.googleapis.com/css2?family=Open+Sans:wght@700;800&family=Questrial&family=Lobster&display=swap">
<style>
  :root {
    --blue: #3f76bf;
    --red: #c8202f;
    --ink: #1c1c1c;
    --paper: #f7f8fa;
    --backdrop: #9a9a9a;
    --van-top: #dfe3e8;
    --van-mid: #b9c0c8;
    --photo-sky: #8fa3b8;
    --photo-body: #e9ebee;
    --photo-ground: #6f7568;
  }
  * { margin: 0; padding: 0; box-sizing: border-box; }
  html, body {
    width: 795px; height: 1200px; overflow: hidden;
    background: var(--backdrop);
  }
  .poster {
    position: absolute; left: 0; top: 44px;
    width: 604px; height: 845px;
    background: var(--paper);
    transform: scale(1.3162);
    transform-origin: top left;
    overflow: hidden;
    font-family: "Questrial", sans-serif;
    color: var(--ink);
  }
  .header-band {
    position: absolute; left: 0; top: 57px; width: 100%; height: 123px;
    background: var(--blue);
  }
  .van-shot {
    position: absolute; left: 207px; top: 7px; width: 227px; height: 123px;
    background: linear-gradient(180deg, var(--van-top), var(--van-mid));
    border-radius: 10px;
  }
  .brand-name {
    position: absolute; left: 0; top: 140px; width: 100%;
    text-align: center;
    font-family: "Open Sans", sans-serif; font-weight: 800;
    color: var(--red);
    line-height: 1;
  }
  .brand-name .brand-main { display: block; font-size: 88px; letter-spacing: -1px; }
  .brand-name .brand-sub { display: block; font-size: 50px; margin-top: 10px; letter-spacing: 1px; }
  .van-photo {
    position: absolute; left: 0; top: 320px; width: 100%; height: 180px;
    background: linear-gradient(100deg, var(--photo-ground) 0%, var(--photo-body) 25%, var(--photo-body) 75%, var(--photo-sky) 100%);
  }
  .services-title {
    position: absolute; left: 0; top: 502px; width: 100%; height: 55px;
    background: var(--blue);
    color: #fff;
    font-family: "Open Sans", sans-serif; font-weight: 700;
    font-size: 35px; text-align: center; line-height: 55px;
    letter-spacing: 0.5px;
  }
  .service-list {
    position: absolute; top: 570px; list-style: none;
    font-size: 15.5px; line-height: 1.05;
  }
  .service-list.left { left: 34px; width: 290px; }
  .service-list.right { left: 328px; width: 270px; }
  .service-list li {
    position: relative; padding-left: 20px; margin-bottom: 17px;
  }
  .service-list li svg {
    position: absolute; left: 0; top: 1px; width: 14px; height: 14px;
  }
  .call-label {
    position: absolute; left: 55px; top: 666px;
    font-family: "Lobster", sans-serif; font-size: 38px; color: var(--red);
  }
  .phone {
    position: absolute; left: 50px; top: 700px; width: 500px;
    font-family: "Lobster", sans-serif; font-size: 80px; color: var(--ink);
    letter-spacing: 1px; line-height: 1.1;
  }
  .footer-band {
    position: absolute; left: 0; top: 800px; width: 100%; height: 45px;
    background: var(--red); color: #fff;
    font-family: "Open Sans", sans-serif; font-weight: 700;
    font-size: 21px; line-height: 45px; text-align: center;
  }
</style>
</head>
<body>
<main class="poster">
  <div class="header-band"></div>
  <div class="van-shot" role="img" aria-label="Photo of the white service van with ladder rack"></div>
  <h1 class="brand-name"><span class="brand-main">Marcels</span><span class="brand-sub">Antenna Service</span></h1>

  <div class="van-photo" role="img" aria-label="Close-up photo of the rear side of the white service van with signwriting"></div>

  <h2 class="services-title">SERVICES WE PROVIDE</h2>

  <svg width="0" height="0" style="position:absolute">
    <defs>
      <symbol id="hex-bullet" viewBox="0 0 14 14">
        <polygon points="3.5,1 10.5,1 14,7 10.5,13 3.5,13 0,7" fill="#c8202f"/>
      </symbol>
    </defs>
  </svg>

  <ul class="service-list left">
    <li><svg><use href="#hex-bullet"/></svg>New home antenna installations</li>
    <li><svg><use href="#hex-bullet"/></svg>repair your dodgy reception</li>
    <li><svg><use href="#hex-bullet"/></svg>Wall mount your big screen TV's</li>
  </ul>
  <ul class="service-list right">
    <li><svg><use href="#hex-bullet"/></svg>add extra outlets</li>
    <li><svg><use href="#hex-bullet"/></svg>Supply and install low cost security camera setups</li>
    <li><svg><use href="#hex-bullet"/></svg>TELVIQ satellite installations</li>
  </ul>

  <p class="call-label">Call us</p>
  <p class="phone">0491 32 60 47</p>

  <p class="footer-band">Anything tv related ,call marcel , he can do it !</p>
</main>
</body>
</html>
```